New Property management company business cards

Looking for a new business card, to reflect new younger ownership
Card should be clean, simple and professional but with a modern layout that is conveys our new logo and business model

Key aspects of the business:

Property Management
Facility Maintenance
Project Management
Tenant Improvements

Mailing Address:
PO BOX 7186
Lindenvale CA, 95382

Phone: 209-614-8837
Direct: 209-614-8831

Doyle Farrant
President

Target Market(s)

Commercial property owners

Industry/Entity Type

Real Estate property management

Contact Information for Business Card

Open to all designs but lean toward vertical layouts

Requirements
Must have
• Logo and space to customize name and contact info

```html
<!DOCTYPE html>
<html lang="en">
<head>
<meta charset="utf-8">
<title>Valcrest Property Management – Business Cards</title>
<link rel="stylesheet" href="https://fonts.googleapis.com/css2?family=Montserrat:wght@400;500;600;700&display=swap">
<style>
  :root {
    --bg: #e9e8e6;
    --card-white: #ffffff;
    --navy: #2b2d3c;
    --navy-deep: #1f2130;
    --teal: #17a89c;
    --text: #3a3b45;
  }
  * { box-sizing: border-box; margin: 0; padding: 0; }
  html, body {
    width: 1200px; height: 786px; overflow: hidden;
    background: var(--bg);
    font-family: "Montserrat", Arial, sans-serif;
    color: var(--text);
  }
  .stage { position: relative; width: 1200px; height: 786px; }
  .card {
    position: absolute; top: 238px;
    width: 540px; height: 309px;
    border-radius: 4px; overflow: hidden;
    box-shadow: 0 10px 28px rgba(0,0,0,.18);
  }
  /* Front */
  .card--front { left: 40px; background: var(--card-white); }
  .brand {
    position: absolute; left: 40px; top: 52px;
    display: flex; align-items: center; gap: 12px;
  }
  .brand__mark { width: 22px; height: 22px; background: var(--teal); flex: none; }
  .brand__name {
    font-size: 34px; font-weight: 500; letter-spacing: 6px;
    color: var(--navy); line-height: 1;
  }
  .person { position: absolute; left: 40px; top: 130px; }
  .person__name { font-size: 23px; font-weight: 700; color: var(--teal); line-height: 1.2; }
  .person__title { font-size: 14px; font-weight: 500; color: var(--navy); margin-top: 2px; }
  .divider {
    position: absolute; left: 40px; top: 188px;
    width: 470px; height: 1.5px; background: var(--teal);
  }
  .contacts {
    position: absolute; left: 40px; top: 202px;
    list-style: none; font-size: 12.5px; line-height: 19px; color: var(--text);
  }
  .contacts li { display: flex; align-items: center; gap: 9px; white-space: nowrap; }
  .contacts svg { width: 11px; height: 11px; fill: var(--navy); flex: none; }
  .mailing {
    position: absolute; left: 338px; top: 204px;
    font-size: 12.5px; line-height: 17px; color: var(--text);
    font-style: normal; white-space: nowrap;
  }
  .front-band { position: absolute; left: 0; bottom: 0; width: 540px; height: 40px; }
  /* Back */
  .card--back { left: 620px; background: var(--navy); }
  .back-pattern {
    position: absolute; inset: 0;
    background: linear-gradient(125deg, #4a4d5c 0%, #2f3141 40%, var(--navy-deep) 100%);
  }
  .back-brand {
    position: absolute; right: 50px; bottom: 110px;
    display: flex; align-items: center; gap: 12px;
  }
  .back-brand .brand__mark { width: 20px; height: 20px; }
  .back-brand .brand__name { font-size: 30px; color: #ffffff; letter-spacing: 5px; }
</style>
</head>
<body>
<main class="stage">

  <section class="card card--front" aria-label="Business card front">
    <div class="brand">
      <span class="brand__mark"></span>
      <span class="brand__name">VALCREST</span>
    </div>

    <div class="person">
      <div class="person__name">Doyle Farrant</div>
      <div class="person__title">President</div>
    </div>

    <div class="divider"></div>

    <ul class="contacts">
      <li>
        <svg viewBox="0 0 12 12"><path d="M2 1h3l1 3-1.5 1a7 7 0 0 0 2.5 2.5L8 6l3 1v3c0 .6-.4 1-1 1A9 9 0 0 1 1 2c0-.6.4-1 1-1z"/></svg>
        209-614-8831
      </li>
      <li>
        <svg viewBox="0 0 12 12"><path d="M3.5 0h5c.6 0 1 .4 1 1v10c0 .6-.4 1-1 1h-5c-.6 0-1-.4-1-1V1c0-.6.4-1 1-1zm.3 1.5v8h4.4v-8z"/></svg>
        209-614-8837
      </li>
      <li>
        <svg viewBox="0 0 12 12"><path d="M0 2h12v8H0zm1 1v.4l5 3.2 5-3.2V3z"/></svg>
        info@valcrestpm.com
      </li>
      <li>
        <svg viewBox="0 0 12 12"><circle cx="6" cy="6" r="5.5"/></svg>
        www.valcrestpm.com
      </li>
    </ul>

    <address class="mailing">
      Mailing Address:<br>
      PO BOX 7186<br>
      Lindenvale CA, 95382
    </address>

    <svg class="front-band" viewBox="0 0 540 40" preserveAspectRatio="none" aria-hidden="true">
      <polygon points="0,30 540,30 540,40 0,40" fill="var(--navy)"/>
      <polygon points="330,14 540,6 540,32 322,32" fill="var(--teal)"/>
    </svg>
  </section>

  <section class="card card--back" aria-label="Business card back">
    <div class="back-pattern" role="img" aria-label="Embossed repeating diamond pattern across the dark card face"></div>
    <div class="back-brand">
      <span class="brand__mark"></span>
      <span class="brand__name">VALCREST</span>
    </div>
  </section>

</main>
</body>
</html>
```